business card for KestrelLine Construction
need a tag line (here to meet your needs)?
business card for KestrelLine Construction -
Creative Brief
Simple
Lorcan Whitlaney
Foreman
New Jersey or servicing north jersey
info@Kestrel-Line.com
www.Kestrel-Line.com
fully licensed fully insured
logo. residential commercial. 24hr emergency service. specializing in: *roofs *chimneys *masonry *gutters
logo. pic of workvan with logo Notes:________________________________________________________________________________________

```html
<!DOCTYPE html>
<html lang="en">
<head>
<meta charset="utf-8">
<title>KestrelLine Construction – Business Card</title>
<link rel="stylesheet" href="https://fonts.googleapis.com/css2?family=Open+Sans:ital,wght@0,400;0,600;0,700;0,800;1,400;1,600;1,700&display=swap">
<style>
  :root {
    --backdrop: #e9e6e1;
    --card: #ffffff;
    --navy: #1f2f8a;
    --navy-deep: #172473;
    --orange: #f39a1e;
    --grey: #6b6f76;
    --divider: #c9ccd2;
  }
  * { margin: 0; padding: 0; box-sizing: border-box; }
  html, body {
    width: 1200px; height: 780px; overflow: hidden;
    background: var(--backdrop);
    font-family: "Open Sans", Arial, sans-serif;
  }
  .card {
    position: absolute; left: 70px; top: 70px;
    width: 1060px; height: 640px;
    background: var(--card);
    border-radius: 40px;
    overflow: hidden;
    box-shadow: 0 6px 24px rgba(0,0,0,0.18);
  }
  .brand {
    position: absolute; left: 0; right: 0; top: 110px;
    display: flex; justify-content: center; align-items: center; gap: 18px;
  }
  .brand-mark { width: 34px; height: 34px; background: var(--orange); }
  .brand-name {
    font-weight: 800; font-size: 62px; color: var(--navy);
    letter-spacing: -1px; line-height: 1;
  }
  .tagline-row {
    position: absolute; left: 70px; right: 70px; top: 212px;
    display: flex; justify-content: space-between;
    font-style: italic; font-weight: 700; font-size: 25px; color: var(--grey);
  }
  .person {
    position: absolute; left: 120px; top: 290px; text-align: right; width: 390px;
  }
  .person-name { font-weight: 700; font-size: 30px; color: var(--navy-deep); }
  .person-role { font-size: 23px; color: var(--orange); margin-top: 2px; }
  .person-area { font-size: 23px; color: var(--grey); margin-top: 22px; }
  .divider {
    position: absolute; left: 545px; top: 285px; width: 2px; height: 200px;
    background: var(--divider);
  }
  .contacts {
    position: absolute; left: 580px; top: 285px; list-style: none;
  }
  .contacts li {
    display: flex; align-items: center; gap: 16px;
    font-size: 23px; color: var(--grey); height: 40px;
  }
  .contacts svg { width: 24px; height: 24px; fill: var(--navy); flex: none; }
  .band { position: absolute; left: 0; bottom: 0; width: 1060px; height: 170px; }
  .specialties {
    position: absolute; left: 0; right: 0; bottom: 24px; text-align: center;
    font-style: italic; font-size: 25px; color: #ffffff; letter-spacing: 0.5px;
  }
</style>
</head>
<body>
  <div class="card">
    <div class="brand">
      <span class="brand-mark"></span>
      <span class="brand-name">KestrelLine Construction</span>
    </div>

    <div class="tagline-row">
      <span class="tagline-sectors">Residential &amp; Commercial.</span>
      <span class="tagline-service">24hr emergency service.</span>
    </div>

    <div class="person">
      <p class="person-name">Lorcan Whitlaney</p>
      <p class="person-role">Foreman</p>
      <p class="person-area">Servicing North Jersey</p>
    </div>

    <div class="divider"></div>

    <ul class="contacts">
      <li><svg viewBox="0 0 24 24"><path d="M6.6 10.8a15.2 15.2 0 0 0 6.6 6.6l2.2-2.2c.3-.3.7-.4 1-.2 1.1.4 2.3.6 3.6.6.6 0 1 .4 1 1V20c0 .6-.4 1-1 1A17 17 0 0 1 3 4c0-.6.4-1 1-1h3.5c.6 0 1 .4 1 1 0 1.3.2 2.5.6 3.6.1.3 0 .7-.2 1z"/></svg>(T)1-888-555-0142</li>
      <li><svg viewBox="0 0 24 24"><path d="M6.6 10.8a15.2 15.2 0 0 0 6.6 6.6l2.2-2.2c.3-.3.7-.4 1-.2 1.1.4 2.3.6 3.6.6.6 0 1 .4 1 1V20c0 .6-.4 1-1 1A17 17 0 0 1 3 4c0-.6.4-1 1-1h3.5c.6 0 1 .4 1 1 0 1.3.2 2.5.6 3.6.1.3 0 .7-.2 1z"/></svg>201-555-0187</li>
      <li><svg viewBox="0 0 24 24"><path d="M12 2a10 10 0 1 0 5 18.7l-.9-1.7A8 8 0 1 1 20 12v1.2c0 1-.7 1.8-1.5 1.8S17 14.2 17 13.2V12a5 5 0 1 0-1.5 3.6A3.4 3.4 0 0 0 18.5 17c2 0 3.5-1.7 3.5-3.8V12A10 10 0 0 0 12 2zm0 13a3 3 0 1 1 0-6 3 3 0 0 1 0 6z"/></svg>info@Kestrel-Line.com</li>
      <li><svg viewBox="0 0 24 24"><path d="M12 2a10 10 0 1 0 0 20 10 10 0 0 0 0-20zm6.9 6h-2.9a15.7 15.7 0 0 0-1.4-3.6A8 8 0 0 1 18.9 8zM12 4c.8 1.2 1.5 2.5 1.9 4h-3.8c.4-1.5 1.1-2.8 1.9-4zM4.3 14a8.2 8.2 0 0 1 0-4h3.4a16.5 16.5 0 0 0 0 4zm.8 2h2.9c.3 1.3.8 2.5 1.4 3.6A8 8 0 0 1 5.1 16zM8 8H5.1a8 8 0 0 1 4.3-3.6C8.8 5.5 8.3 6.7 8 8zm4 12c-.8-1.2-1.5-2.5-1.9-4h3.8c-.4 1.5-1.1 2.8-1.9 4zm2.3-6H9.7a14.7 14.7 0 0 1 0-4h4.6a14.7 14.7 0 0 1 0 4zm.3 5.6c.6-1.1 1.1-2.3 1.4-3.6h2.9a8 8 0 0 1-4.3 3.6zm1.7-5.6a16.5 16.5 0 0 0 0-4h3.4a8.2 8.2 0 0 1 0 4z"/></svg>www.Kestrel-Line.com</li>
    </ul>

    <svg class="band" viewBox="0 0 1060 170" preserveAspectRatio="none" aria-hidden="true">
      <path d="M0 60 Q 530 20 1060 30 L1060 44 Q 530 36 0 78 Z" fill="var(--orange)"/>
      <path d="M0 86 Q 530 44 1060 48 L1060 170 L0 170 Z" fill="var(--navy)"/>
    </svg>
    <p class="specialties">Specializing in : roofs / chimneys / masonry / gutters</p>
  </div>
</body>
</html>
```